Website Design for a "Talent Recruitment Agency"

We are looking for a website design for the website of our "Talent Recruitment Agency"; which is called "Crestline Circle".
Our recruitment website "Crestline Circle" will be focusing on: "Crestline Circle: Bridging People & Employers in Switzerland"; which means our target audience is two-folded:
(i) TALENT - that is currently residing in- or outside of Switzerland, and is open for and interested in the "Swiss Job Market".
(ii) COMPANIES - that are looking for talent for specific job vacancies in Switzerland.
With our "Crestline Circle" approach we inted to focus on Membership & Partnership:
(a)"Membership"(TALENT)
and
(b)"Partnership"(COMPANIES)
Some of the competitor sites we like are:
• www.brimlo42.dk
• www.qazet.ch
• www.plovik.ch/en
A sitemap example of our website is attached.
Also attached is a "Crestline Circle" logo in .eps format and one in .jpeg format.
We very much look forward to receive your creative ideas.
Best regards,
Crestline Circle
Crestline Circle: Bridging People & Employers in Switzerland.
Website: crestlinecircle.ch - Twitter: CrestlineCircleCH
Target Market(s)
(i) TALENT (with around 0-10 years of working experience), currently residing in- or outside of Switzerland, but eligible to work in Switzerland.
(ii) COMPANIES (national or international) that are based in Switzerland.
Industry/Entity Type
Recruitment

```html
<!DOCTYPE html>
<html lang="en">
<head>
<meta charset="utf-8">
<title>Crestline Circle</title>
<link rel="stylesheet" href="https://fonts.googleapis.com/css2?family=Open+Sans:wght@300;400;600;700&family=Oswald:wght@300;400&display=swap">
<style>
:root{
  --blue:#1589c0;
  --blue-dark:#0d6a97;
  --blue-soft:#4fa3d3;
  --orange:#f08b3b;
  --orange-deep:#e9782a;
  --ink:#4a4a4a;
  --grey:#8a8a8a;
  --rule:#dcdcdc;
  --topbar:#e9f0f6;
  --field:#eaf3fa;
  --white:#ffffff;
}
*{box-sizing:border-box;margin:0;padding:0}
html,body{width:989px;height:1200px;overflow:hidden;background:var(--white)}
body{position:relative;font-family:"Open Sans",sans-serif;color:var(--ink)}
.abs{position:absolute}

/* top bar */
.topbar{left:0;top:0;width:989px;height:26px;background:var(--topbar)}
.lang{left:104px;top:6px;font-size:7px;letter-spacing:.3px;color:#666;display:flex;align-items:center;gap:6px}
.lang-select{width:76px;height:13px;background:var(--white);border:1px solid #cfd8e0;display:flex;align-items:center;gap:4px;padding-left:3px;font-size:7px}
.lang-flag{width:10px;height:7px;background:#3a5a9a}
.lang-caret{margin-left:auto;margin-right:4px;width:0;height:0;border-left:3px solid transparent;border-right:3px solid transparent;border-top:4px solid var(--blue)}
.top-social{right:40px;top:6px;display:flex;gap:10px}
.top-social span{width:11px;height:11px;background:var(--blue);border-radius:2px}
.top-social span:nth-child(3){background:#d23c2f;width:20px}
.top-social span:last-child{background:var(--orange)}

/* header */
.header{left:0;top:26px;width:989px;height:100px;background:var(--white)}
.brand{left:57px;top:52px;display:flex;align-items:center;gap:10px;font-size:24px;font-weight:600;color:var(--orange)}
.brand-dot{width:34px;height:34px;border-radius:50%;background:var(--blue)}
.nav{left:480px;top:48px;display:flex;font-family:"Oswald",sans-serif;font-weight:300;font-size:12px;color:#555}
.nav a{color:inherit;text-decoration:none;display:block;text-align:center}
.nav .current{color:#333}
.nav-rule{left:468px;top:92px;width:492px;height:1px;background:#eee}
.nav-pointer{left:498px;top:92px;width:0;height:0;border-left:7px solid transparent;border-right:7px solid transparent;border-top:7px solid #e6e6e6}

/* hero */
.hero{left:0;top:126px;width:989px;height:338px;background:linear-gradient(90deg,#e6e3e0 0%,#f3f4f6 30%,#f8f9fb 55%,#eceef1 100%)}
.hero-photo{left:520px;top:140px;width:320px;height:324px;background:radial-gradient(ellipse 60% 70% at 50% 70%,rgba(40,40,44,.55) 0%,rgba(60,60,66,.25) 55%,rgba(240,241,243,0) 100%)}
.hero-arrow{top:266px;width:30px;height:29px;background:#f4f4f4;border:1px solid #d8d8d8;border-radius:3px;display:flex;align-items:center;justify-content:center}
.hero-arrow.left{left:22px}
.hero-arrow.right{left:934px}
.hero-tag{left:145px;color:var(--white);font-weight:300;white-space:nowrap}
.hero-tag.line1{top:262px;background:var(--orange);font-size:21px;padding:4px 12px 5px}
.hero-tag.line2{top:302px;background:var(--orange);font-size:21px;padding:4px 12px 5px}
.hero-tag.sub{top:344px;background:var(--blue-soft);font-size:15px;padding:4px 12px}

/* blue band */
.band{left:0;top:464px;width:989px;height:459px;background:var(--blue)}
.band-shadow{left:0;top:464px;width:989px;height:10px;background:linear-gradient(180deg,rgba(0,0,0,.18),transparent)}
.col-divider{left:346px;top:506px;width:1px;height:370px;background:linear-gradient(180deg,transparent,rgba(0,0,0,.15),transparent)}
.on-blue{color:var(--white)}
.about-title{left:36px;top:512px;font-size:21px;font-weight:700}
.about-sub{left:36px;top:542px;font-size:14.5px;font-weight:300}
.copy{font-size:10.8px;line-height:16px}
.about-copy{left:36px;top:580px;width:280px}
.more{display:inline-flex;align-items:center;gap:5px;height:17px;padding:0 9px;border-radius:9px;background:var(--blue-dark);font-family:"Oswald",sans-serif;font-weight:300;font-size:8.5px;color:var(--white)}
.more::after{content:"";width:0;height:0;border-top:3px solid transparent;border-bottom:3px solid transparent;border-left:3px solid #5fa9d2}
.about-more{left:36px;top:642px}
.left-rule{left:36px;top:677px;width:276px;height:1px;background:rgba(255,255,255,.22)}
.signup-title{left:36px;top:694px;font-size:15px;font-weight:600;letter-spacing:.2px}
.field-label{left:36px;font-size:10.5px;line-height:13px}
.field{left:106px;width:157px;background:var(--field)}
.file-btn{left:106px;top:842px;width:72px;height:18px;background:#e8e8e8;border:1px solid #aaa;border-radius:2px;color:#333;font-size:9.5px;display:flex;align-items:center;justify-content:center}
.file-note{left:185px;top:845px;font-size:9.5px}
.submit{left:104px;top:871px;width:58px;height:18px;border-radius:9px;background:var(--blue-dark);font-family:"Oswald",sans-serif;font-size:10px;display:flex;align-items:center;justify-content:center}
.feature-icon{width:34px;height:28px}
.feature-title{font-family:"Oswald",sans-serif;font-weight:300;font-size:16px}
.feature-copy{width:270px}

/* clients */
.clients-title{left:38px;top:987px;font-family:"Oswald",sans-serif;font-weight:400;font-size:13px;color:#555}
.pager{top:996px;width:12px;height:12px}
.pager.prev{left:924px;background:#b9dbef}
.pager.next{left:941px;background:var(--blue)}
.clients-rule{left:36px;width:916px;height:1px;background:var(--rule)}
.clients-row{left:36px;top:1025px;width:916px;height:72px;display:flex}
.client{flex:1;display:flex;align-items:center;justify-content:center;font-size:24px;font-weight:700;color:#9a9a9a;border-right:1px dashed #d6d6d6}
.client:last-child{border-right:none}

/* footer */
.footer{left:0;top:1162px;width:989px;height:38px;background:var(--orange);border-top:2px solid var(--orange-deep)}
.foot-links{left:39px;top:1175px;font-family:"Oswald",sans-serif;font-weight:300;font-size:9.5px;color:var(--white)}
.foot-social{left:230px;top:1176px;display:flex;gap:11px}
.foot-social span{width:10px;height:10px;background:var(--white);border-radius:2px;opacity:.9}
.foot-brand{left:800px;top:1170px;display:flex;align-items:center;gap:7px;color:var(--white);font-weight:700;font-size:15px}
.foot-brand i{width:22px;height:22px;border-radius:50%;background:var(--white)}
</style>
</head>
<body>

<div class="abs topbar"></div>
<div class="abs lang">LANGUAGE <div class="lang-select"><span class="lang-flag"></span>ENGLISH<span class="lang-caret"></span></div></div>
<div class="abs top-social"><span></span><span></span><span></span><span></span><span></span></div>

<header class="abs header"></header>
<div class="abs brand"><span class="brand-dot"></span>Crestline Circle</div>
<nav class="abs nav">
  <a class="current" style="width:52px">HOME</a>
  <a style="width:65px">ABOUT</a>
  <a style="width:67px">TALENT</a>
  <a style="width:92px">COMPANIES</a>
  <a style="width:66px">JOBS</a>
  <a style="width:72px">EVENTS</a>
  <a style="width:84px">CONTACT</a>
</nav>
<div class="abs nav-rule"></div>
<div class="abs nav-pointer"></div>

<section class="abs hero" role="img" aria-label="Softly blurred bright office interior"></section>
<div class="abs hero-photo" role="img" aria-label="Photo of a smiling professional in a dark suit"></div>
<div class="abs hero-arrow left"><svg width="8" height="10"><path d="M7 0 L0 5 L7 10Z" fill="#999"/></svg></div>
<div class="abs hero-arrow right"><svg width="8" height="10"><path d="M1 0 L8 5 L1 10Z" fill="#999"/></svg></div>
<div class="abs hero-tag line1">Crestline Circle: Bridging People</div>
<div class="abs hero-tag line2">&amp; Employers in Switzerland</div>
<div class="abs hero-tag sub">Sed ut perspiciatis unde omnis iste natus..</div>

<section class="abs band"></section>
<div class="abs band-shadow"></div>
<div class="abs col-divider"></div>

<h2 class="abs about-title on-blue">About Us</h2>
<p class="abs about-sub on-blue">At Vero Eos et Accusamus et Iusto Odio</p>
<p class="abs copy about-copy on-blue">Temporibus autem quibusdam et aut officiis debitis aut rerum necessitatibus saepe eveniet ut et voluptates repudiandae sint et molestiae non recusandae...</p>
<span class="abs more about-more">Learn more</span>
<div class="abs left-rule"></div>

<h3 class="abs signup-title on-blue">Sign Up for the Crestline Circle</h3>
<label class="abs field-label on-blue" style="top:740px">Name:</label>
<div class="abs field" style="top:737px;height:20px"></div>
<label class="abs field-label on-blue" style="top:766px">Email:</label>
<div class="abs field" style="top:763px;height:20px"></div>
<label class="abs field-label on-blue" style="top:792px">How can we<br>help you?</label>
<div class="abs field" style="top:790px;height:44px"></div>
<label class="abs field-label on-blue" style="top:845px">CV:</label>
<div class="abs file-btn">Choose File</div>
<div class="abs file-note on-blue">No Chosen File</div>
<div class="abs submit on-blue">SUBMIT</div>

<svg class="abs feature-icon" style="left:389px;top:514px" viewBox="0 0 34 28"><circle cx="16" cy="12" r="10" fill="none" stroke="#d7ecf8" stroke-width="3"/><circle cx="16" cy="10" r="3.5" fill="#d7ecf8"/><path d="M10 18 Q16 12 22 18Z" fill="#d7ecf8"/><path d="M23 19 L30 26" stroke="#d7ecf8" stroke-width="4" stroke-linecap="round"/></svg>
<h3 class="abs feature-title on-blue" style="left:389px;top:554px">Talent</h3>
<p class="abs copy feature-copy on-blue" style="left:389px;top:588px">At vero eos et accusamus et iusto odio dignissimos ducimus qui blanditiis praesentium voluptatum deleniti atque</p>
<span class="abs more" style="left:389px;top:651px">Learn more</span>

<svg class="abs feature-icon" style="left:684px;top:514px" viewBox="0 0 34 28"><rect x="2" y="8" width="12" height="20" fill="#d7ecf8"/><rect x="12" y="2" width="14" height="26" fill="#d7ecf8"/><rect x="24" y="10" width="8" height="18" fill="#d7ecf8"/><g fill="#1589c0"><rect x="15" y="6" width="3" height="3"/><rect x="20" y="6" width="3" height="3"/><rect x="15" y="12" width="3" height="3"/><rect x="20" y="12" width="3" height="3"/><rect x="15" y="18" width="3" height="3"/><rect x="20" y="18" width="3" height="3"/><rect x="5" y="12" width="3" height="3"/><rect x="5" y="18" width="3" height="3"/></g></svg>
<h3 class="abs feature-title on-blue" style="left:684px;top:554px">Companies</h3>
<p class="abs copy feature-copy on-blue" style="left:684px;top:588px">Temporibus autem quibusdam et aut officiis debitis aut rerum necessitatibus saepe eveniet ut et volup tates repudiandae sint...</p>
<span class="abs more" style="left:684px;top:651px">Learn more</span>

<svg class="abs feature-icon" style="left:389px;top:716px" viewBox="0 0 34 28"><circle cx="11" cy="8" r="5" fill="#d7ecf8"/><circle cx="23" cy="8" r="5" fill="#d7ecf8"/><path d="M1 27 Q1 15 11 15 Q21 15 21 27Z" fill="#d7ecf8"/><path d="M13 27 Q13 15 23 15 Q33 15 33 27Z" fill="#d7ecf8"/></svg>
<h3 class="abs feature-title on-blue" style="left:389px;top:759px">Membership</h3>
<p class="abs copy feature-copy on-blue" style="left:389px;top:793px">Itaque earum rerum hic tenetur a sapiente delectus, ut aut reiciendis voluptatibus maiores alias consequatur...</p>
<span class="abs more" style="left:389px;top:856px">Learn more</span>

<svg class="abs feature-icon" style="left:684px;top:716px" viewBox="0 0 34 28"><path d="M2 10 L10 4 L17 9 L24 4 L32 10 L24 20 L17 24 L10 20Z" fill="none" stroke="#d7ecf8" stroke-width="3" stroke-linejoin="round"/><path d="M11 13 L17 18 L23 13" fill="none" stroke="#d7ecf8" stroke-width="2.5"/></svg>
<h3 class="abs feature-title on-blue" style="left:684px;top:759px">Partnership</h3>
<p class="abs copy feature-copy on-blue" style="left:684px;top:793px">Neque porro quisquam est, qui dolorem ipsum quia dolor sit amet, consectetur, adipisci velit, sed quia non numquam eius...</p>
<span class="abs more" style="left:684px;top:856px">Learn more</span>

<h2 class="abs clients-title">OUR CLIENTS</h2>
<div class="abs pager prev"></div>
<div class="abs pager next"></div>
<div class="abs clients-rule" style="top:1015px"></div>
<div class="abs clients-row">
  <div class="client">Halden</div>
  <div class="client">Norvessa</div>
  <div class="client">Telvani</div>
  <div class="client">Kestrel</div>
  <div class="client">Arvik</div>
</div>
<div class="abs clients-rule" style="top:1106px"></div>

<footer class="abs footer"></footer>
<div class="abs foot-links">Home &nbsp;|&nbsp; About &nbsp;|&nbsp; FAQ &nbsp;|&nbsp; Services &nbsp;|&nbsp; Contact</div>
<div class="abs foot-social"><span></span><span></span><span></span><span></span><span></span></div>
<div class="abs foot-brand"><i></i>Crestline Circle</div>

</body>
</html>
```